3"x8" Flyer (double sided) for Roofing Company (example flyers attached)

We are getting ready to advertise with a company called "CouponMate" and our advertisement includes a 3"x8" DOUBLE SIDED insert. (see competitor attachments for samples)

NOTE... We may require a few minor revisions from the winning designer.

About Us...

We offer roofing, windows, siding, insulation in the West Michigan area.

Company info...

Company name: Thornbury Home Works
Address: 2863 North Kestrel Blvd N.E., Wyoming, MI 49371
Phone: 616.473.0158
Website: www.thornburyhomeworks.net
Updates

"Financing" badge I refer too in each of your feedbacks can be see at http://thornburyhw.net/badge.jpg

Target Market(s)

US Homeowners 35-65 years old with good credit, nice houses in need of home improvements.

Industry/Entity Type

Insulation

Requirements
Must have
• Flyer should be 3"x8" DOUBLE SIDED

(you can be creative but we do need some images of roofs or full houses, see attachments for samples)

Some items to include on flyer. These are in no particular order and can be placed anywhere...

-Fast FREE Estimates
-CTR logo with A+ shown
-100% financing and 12 months same as cash with approved credit
-30+ Years in business
-100% satisfaction guaranteed (icon)
-Lifetime warranty roofing materials made in MICHIGAN
-Locally owned and operated
-Licensed and Insured

Nice to have
• Also, I'd like to fit a small bullet point list somewhere that list our other services "Roofing, Siding, Windows, Doors, Insulation, Remodeling

```html
<!DOCTYPE html>
<html lang="en">
<head>
<meta charset="utf-8">
<title>Thornbury Home Works – Flyer</title>
<link href="https://fonts.googleapis.com/css2?family=Ubuntu:ital,wght@0,400;0,500;0,700;1,400&display=swap" rel="stylesheet">
<style>
  :root {
    --sky-light: #cfe6f6;
    --sky-mid: #a9d3f0;
    --sky-deep: #7cbde8;
    --brand-brown: #8a5a2b;
    --tile-border: #a57c52;
    --ink: #333333;
    --ink-dark: #262626;
    --white: #ffffff;
    --box-top: #5e5e5e;
    --box-bottom: #1c1c1c;
    --yellow: #f4e20a;
    --green: #7bd13f;
    --sky-text: #5fb4ef;
    --seal-green: #2f9a2f;
    --seal-light: #5cc04a;
    --badge-blue: #1d5f9e;
  }
  * { box-sizing: border-box; margin: 0; padding: 0; }
  html, body { width: 1200px; height: 900px; overflow: hidden; background: var(--white); }
  body { position: relative; font-family: "Ubuntu", sans-serif; color: var(--ink); }

  .side { position: absolute; left: 62px; width: 1074px; height: 402px; overflow: hidden; }
  .side--front { top: 35px; background: linear-gradient(180deg, var(--sky-mid) 0%, var(--sky-light) 60%, var(--sky-mid) 100%); }
  .side--back { top: 456px; background: linear-gradient(180deg, var(--sky-deep) 0%, var(--sky-light) 45%, var(--sky-mid) 100%); }

  /* front */
  .brand { position: absolute; left: 36px; top: 38px; display: flex; align-items: center; gap: 7px; }
  .brand__mark { width: 14px; height: 14px; background: var(--brand-brown); }
  .brand__name { font-size: 15px; font-weight: 700; color: var(--brand-brown); }
  .address { position: absolute; left: 36px; top: 99px; font-size: 11px; font-style: italic; line-height: 13px; color: var(--ink); }
  .gable { position: absolute; left: 0; top: 0; }
  .website { position: absolute; left: 150px; top: 316px; font-size: 11.5px; font-weight: 500; color: var(--ink-dark); transform: rotate(-36deg); transform-origin: left top; white-space: nowrap; }

  .service { position: absolute; width: 209px; height: 128px; border: 2px solid var(--tile-border); border-radius: 10px; overflow: hidden; box-shadow: 0 1px 3px rgba(0,0,0,0.2); }
  .service__photo { position: absolute; inset: 0; }
  .service__label { position: absolute; left: 0; right: 0; top: 74px; height: 40px; background: rgba(255,255,255,0.7); font-size: 20px; font-weight: 700; color: var(--ink); display: flex; align-items: center; justify-content: center; }
  .service--insulation { left: 611px; top: 88px; }
  .service--insulation .service__photo { background:
      linear-gradient(90deg, transparent 45%, rgba(120,100,80,0.35) 48%, transparent 52%),
      linear-gradient(180deg, #d9d6d0 0%, #f4efe6 35%, #c4ab86 60%, #8e7a60 100%); }
  .service--windows { left: 838px; top: 88px; }
  .service--windows .service__photo { background:
      linear-gradient(90deg, #ecebe4 0%, #ffffff 30%, #e6e2d8 55%, #f7f5ef 75%, #cfc8b6 100%); }
  .service--roofing { left: 611px; top: 240px; }
  .service--roofing .service__photo { background: linear-gradient(180deg, #d5dde2 0%, #c7cdd0 14%, #5d554e 24%, #6e655c 42%, #d9d6d0 55%, #b7b0a7 80%, #8f877d 100%); }
  .service--siding { left: 838px; top: 240px; }
  .service--siding .service__photo { background:
      linear-gradient(150deg, #c9dbe6 0%, #e7edf0 25%, #ffffff 40%, #d6d3cc 60%, #efeee9 80%, #c3bfb4 100%); }
  .seal { position: absolute; left: 964px; top: 34px; }

  /* back */
  .services-line { position: absolute; left: 0; width: 1074px; top: 35px; text-align: center; font-size: 19.5px; font-weight: 500; color: var(--white); white-space: nowrap; text-shadow: 0 0 2px rgba(0,60,120,0.25); }
  .services-line--reflect { top: 53px; transform: scaleY(-1); opacity: 0.28; text-shadow: none; }
  .call { position: absolute; left: 142px; top: 95px; font-size: 31px; font-weight: 700; color: var(--ink); letter-spacing: 0.6px; white-space: nowrap; }
  .perk { position: absolute; top: 167px; width: 157px; height: 179px; background: linear-gradient(180deg, var(--box-top), var(--box-bottom)); border: 1px solid #8a8a8a; box-shadow: 0 8px 8px rgba(0,0,0,0.22); display: flex; flex-direction: column; align-items: center; justify-content: center; text-align: center; color: var(--white); }
  .perk--estimates { left: 42px; font-size: 22px; font-weight: 500; line-height: 28px; }
  .perk--estimates .accent { color: var(--yellow); }
  .perk--warranty { left: 219px; font-size: 15.5px; font-weight: 500; line-height: 19px; }
  .perk--warranty .accent { color: var(--green); font-size: 21px; font-weight: 400; line-height: 28px; }
  .perk--years { left: 397px; font-size: 15.5px; font-weight: 500; line-height: 19px; }
  .perk--years .accent { color: var(--sky-text); font-size: 22px; line-height: 26px; }
  .perk--years .accent-sub { color: var(--sky-text); font-size: 14.5px; margin-bottom: 4px; }
  .perk--licensed { left: 575px; font-size: 22px; font-weight: 500; line-height: 29px; }
  .tick { position: absolute; left: 693px; top: 130px; }
  .financing { position: absolute; left: 138px; top: 358px; font-size: 16.3px; font-weight: 500; color: var(--ink); white-space: nowrap; }
  .roof-corner { position: absolute; left: 0; top: 0; }
  .rating-badge { position: absolute; left: 933px; top: 322px; }
</style>
</head>
<body>

<section class="side side--front" aria-label="Flyer front">
  <svg class="gable" width="1074" height="402" viewBox="0 0 1074 402">
    <defs>
      <linearGradient id="brick" x1="0" y1="0" x2="1" y2="1">
        <stop offset="0" stop-color="#6f6a63"/>
        <stop offset="0.4" stop-color="#958b80"/>
        <stop offset="0.7" stop-color="#7f776c"/>
        <stop offset="1" stop-color="#a0968a"/>
      </linearGradient>
    </defs>
    <polygon role="img" aria-label="Photo of a brick house gable with a small window" points="92,402 560,58 583,58 583,402" fill="url(#brick)"/>
    <polygon points="68,402 558,46 583,46 583,62 560,62 92,402" fill="#1f2430"/>
  </svg>
  <div class="brand"><span class="brand__mark"></span><span class="brand__name">Thornbury Home Works</span></div>
  <p class="address">Thornbury Home Works<br>2863 North Kestrel Blvd N.E.,<br>Wyoming, MI 49371</p>
  <p class="website">www.thornburyhomeworks.net</p>

  <div class="service service--insulation"><div class="service__photo" role="img" aria-label="Photo of a framed attic being insulated"></div><div class="service__label">Insulation</div></div>
  <div class="service service--windows"><div class="service__photo" role="img" aria-label="Photo of a bright room with new windows"></div><div class="service__label">Windows</div></div>
  <div class="service service--roofing"><div class="service__photo" role="img" aria-label="Photo of a shingled house roof"></div><div class="service__label">Roofing</div></div>
  <div class="service service--siding"><div class="service__photo" role="img" aria-label="Photo of white siding gables"></div><div class="service__label">Siding</div></div>

  <svg class="seal" width="100" height="100" viewBox="0 0 100 100" aria-label="100% satisfaction guaranteed">
    <defs>
      <radialGradient id="sealFill" cx="0.4" cy="0.35" r="0.7">
        <stop offset="0" stop-color="var(--seal-light)"/>
        <stop offset="1" stop-color="var(--seal-green)"/>
      </radialGradient>
      <path id="sealArc" d="M22,52 A28,28 0 0 1 78,52"/>
    </defs>
    <polygon fill="url(#sealFill)" points="50,3 56,12 66,6 69,17 80,15 79,26 90,28 85,38 95,44 87,51 94,60 84,64 87,75 76,75 75,86 65,83 60,93 52,86 44,94 39,84 28,88 27,77 16,77 19,66 8,62 15,53 6,46 16,40 11,30 22,28 21,17 32,19 35,8 45,13"/>
    <g transform="rotate(-32 50 50)">
      <text font-family="Ubuntu, sans-serif" font-size="6" fill="#ffffff"><textPath href="#sealArc" startOffset="50%" text-anchor="middle">satisfaction guaranteed</textPath></text>
      <text x="50" y="64" text-anchor="middle" font-family="Ubuntu, sans-serif" font-size="25" fill="#ffffff">100%</text>
    </g>
  </svg>
</section>

<section class="side side--back" aria-label="Flyer back">
  <svg class="roof-corner" width="1074" height="402" viewBox="0 0 1074 402">
    <defs>
      <linearGradient id="shingle" x1="0" y1="0" x2="1" y2="1">
        <stop offset="0" stop-color="#b4653a"/>
        <stop offset="0.5" stop-color="#9a4d2c"/>
        <stop offset="1" stop-color="#6e3520"/>
      </linearGradient>
    </defs>
    <polygon role="img" aria-label="Photo of a red shingled roof edge" points="772,402 1074,104 1074,402" fill="url(#shingle)"/>
    <line x1="776" y1="402" x2="1074" y2="110" stroke="#d4cdc2" stroke-width="5"/>
    <line x1="790" y1="402" x2="1074" y2="124" stroke="#8a7f73" stroke-width="2"/>
  </svg>

  <p class="services-line">Roofing • Siding • Windows • Doors • Insulation • Remodeling</p>
  <p class="services-line services-line--reflect" aria-hidden="true">Roofing • Siding • Windows • Doors • Insulation • Remodeling</p>
  <h1 class="call">CALL US TODAY 616 - 473 - 0158</h1>

  <div class="perk perk--estimates"><span>FAST</span><span class="accent">FREE</span><span>ESTIMATES</span></div>
  <div class="perk perk--warranty"><span class="accent">Lifetime<br>Warranty</span><span>Roofing materials<br>made in MICHIGAN</span></div>
  <div class="perk perk--years"><span class="accent">30+ Years</span><span class="accent-sub">in business</span><span>Locally owned<br>and operated</span></div>
  <div class="perk perk--licensed"><span>Licensed<br>and<br>Insured</span></div>

  <svg class="tick" width="68" height="68" viewBox="0 0 68 68" aria-hidden="true">
    <defs>
      <linearGradient id="rim" x1="0" y1="0" x2="0" y2="1">
        <stop offset="0" stop-color="#f2f2f2"/>
        <stop offset="1" stop-color="#9a9a9a"/>
      </linearGradient>
      <radialGradient id="tickFill" cx="0.4" cy="0.3" r="0.75">
        <stop offset="0" stop-color="#4c9a4a"/>
        <stop offset="1" stop-color="#123d1c"/>
      </radialGradient>
    </defs>
    <circle cx="34" cy="34" r="33" fill="url(#rim)"/>
    <circle cx="34" cy="34" r="26" fill="url(#tickFill)"/>
    <path d="M21 35 L30 44 L48 24" fill="none" stroke="#ffffff" stroke-width="6" stroke-linecap="round" stroke-linejoin="round"/>
  </svg>

  <p class="financing">100% financing and 12 months same as cash with approved credit</p>

  <svg class="rating-badge" width="110" height="44" viewBox="0 0 110 44" aria-label="Accreditation badge">
    <rect x="1" y="1" width="108" height="42" rx="5" fill="#ffffff"/>
    <rect x="4" y="4" width="26" height="36" rx="3" fill="var(--badge-blue)"/>
    <rect x="32" y="4" width="74" height="36" rx="3" fill="var(--badge-blue)"/>
  </svg>
</section>

</body>
</html>
```